Calm Steering Manual - document template and logo

I am an ADHD Coach for adult professionals, and I have created a Steering Manual on supporting employees who have ADHD. I want this guide to look professional and polished as I have a lot of interest in it, also from corporate clients, and would also like to be able to share in to a wider audience as part of my self-marketing on social media platforms. At the moment I am an independant coach, just 'winging it' based on word of mouth recommendations, so I don't even have a business design or logo etc yet, so I can't really provide that as inspiration. However, this means I am pretty open to how the design is. For the logo.. I love gardening, and this is reflected in how I show up on social media, so I was thinking of maybe a seed coming out of the earth style of logo - I am warm, nurturing but still love my job in corporate and doing executive and team coaching.

Target Market(s)

Corporate people leaders - the type of leaders that are genuinely interested in being inclusive and creating safe environments for their teams.

Industry/Entity Type

Pharma mainly, but not exclusively.

Font styles to use
Serif
Sans Serif

Colors

Designer to choose colors to be used in the design.

Requirements
Must have
• It should have a professional corporate, but still personal warm, friendly feel. I like earthy, natural tones
Should not have
• Anything childish.

```html
<!DOCTYPE html>
<html lang="en">
<head>
<meta charset="utf-8">
<title>Calm Steering Manual – document pages</title>
<link href="https://fonts.googleapis.com/css2?family=Work+Sans:ital,wght@0,400;0,500;0,600;0,700;1,400&display=swap" rel="stylesheet">
<style>
:root{
  --brown:#6e3d2c;
  --teal:#1fb2a3;
  --ink:#2e2e2e;
  --stage:#7a7a7a;
  --paper:#ffffff;
}
*{box-sizing:border-box;margin:0;padding:0}
html,body{width:1200px;height:2196px;overflow:hidden;background:var(--stage)}
body{position:relative;font-family:"Work Sans",Arial,sans-serif;color:var(--ink)}
.page{position:absolute;width:369px;height:521px;background:var(--paper);overflow:hidden}
.c1{left:32px}.c2{left:414px}.c3{left:796px}
.r1{top:29px}.r2{top:563px}.r3{top:1097px}.r4{top:1632px}

/* running header */
.head{position:absolute;left:30px;right:30px;top:12px;height:16px;border-bottom:.6px solid #999;display:flex;justify-content:space-between;align-items:flex-end;padding-bottom:2px}
.head .tag{font-style:italic;font-size:4.4px}
.brand{display:inline-flex;align-items:center;gap:2px;font-weight:700;color:var(--brown);font-size:9px;line-height:1}
.brand .dot{width:7px;height:7px;border-radius:50%;background:var(--teal)}

/* body */
.body{position:absolute;left:32px;right:30px;top:36px;font-size:5.1px;line-height:1.5}
.body p{margin-bottom:5px}
.sec{position:relative;font-size:9.4px;font-weight:500;color:var(--brown);margin:9px 0 7px}
.sec::before{content:"";position:absolute;left:-32px;top:1px;width:27px;height:8px;background:var(--brown)}
.sec span{color:var(--teal)}
.sub{font-size:6px;font-weight:600;margin:6px 0 3px}
b{font-weight:700}
.tick{display:inline-block;width:4.4px;height:4.4px;border:.6px solid var(--ink);border-radius:50%;margin-right:1.5px;vertical-align:-.5px}

/* footer wave */
.foot{position:absolute;left:0;bottom:0;width:369px;height:100px}
.foot-text{position:absolute;bottom:10px;left:30px;right:24px;display:flex;justify-content:space-between;color:#fff;font-size:4.6px}

/* cover */
.cover-photo{position:absolute;left:0;top:0}
.cover-brand{position:absolute;left:26px;top:330px;font-size:40px;gap:6px}
.cover-brand .dot{width:30px;height:30px}
.cover-title{position:absolute;left:24px;top:422px;width:228px;text-align:right;color:var(--brown);font-weight:700;font-size:30px;line-height:1}
.cover-sub{position:absolute;left:30px;top:486px;font-size:10.5px;font-weight:500;letter-spacing:.2px}
.author{position:absolute;left:254px;top:456px;width:100px;font-size:5.4px;line-height:1.45}
.author::before{content:"";display:block;width:90px;height:2px;background:var(--teal);margin-bottom:4px}
.author .name{font-size:8px;font-weight:700}
.author .role{font-size:7px;margin-bottom:4px}

/* table of contents */
.toc{font-size:6.6px;line-height:1.62}
.toc li{list-style:none;display:flex;align-items:baseline}
.toc li .t{white-space:nowrap}
.toc li .fill{flex:1;border-bottom:.6px solid var(--ink);margin:0 3px}
.toc li.main{font-weight:600}
.toc li.lv2{padding-left:21px}

ul.keys{margin:2px 0 6px 14px}
ul.keys li{margin-bottom:2px}

/* back cover */
.back-ring{position:absolute;left:72px;top:100px;width:222px;height:222px;border:1.2px solid var(--brown);border-radius:50%}
.back-photo{position:absolute;left:81px;top:109px;width:204px;height:204px;border-radius:50%;background:radial-gradient(circle at 40% 35%,#9fc5dc,#bcd6e3 55%,#d8e7ee)}
.back-brand{position:absolute;left:110px;top:196px;font-size:30px;gap:5px}
.back-brand .dot{width:24px;height:24px}
.back-text{position:absolute;left:0;right:0;top:380px;text-align:center;font-size:7px;font-weight:600;line-height:1.2}
.back-text .who{margin-top:10px;font-size:7px}
.back-text .who span{font-weight:400;font-size:6px}
.back-text .contact{font-size:4.8px;margin-top:4px;font-weight:400}
</style>
</head>
<body>
<svg width="0" height="0" style="position:absolute">
  <defs>
    <linearGradient id="bandFill" x1="0" x2="1" y1="0" y2="0">
      <stop offset="0" stop-color="#6e3d2c"/>
      <stop offset=".55" stop-color="#6e3d2c"/>
      <stop offset=".88" stop-color="#1fb2a3"/>
    </linearGradient>
    <symbol id="wave" viewBox="0 0 369 100" preserveAspectRatio="none">
      <path d="M0 32 Q190 6 369 2 V8 Q190 14 0 40Z" fill="#1fb2a3"/>
      <path d="M0 44 Q190 18 369 12 V100 H0Z" fill="url(#bandFill)"/>
    </symbol>
  </defs>
</svg>

<!-- Cover -->
<section class="page c1 r1">
  <svg class="cover-photo" width="369" height="330" viewBox="0 0 369 330">
    <defs>
      <clipPath id="coverClip"><circle cx="170" cy="60" r="250"/></clipPath>
      <linearGradient id="coverPhoto" x1="0" y1="0" x2="0" y2="1">
        <stop offset="0" stop-color="#cfe3ee"/><stop offset=".55" stop-color="#b7d0c5"/><stop offset="1" stop-color="#c9b9a6"/>
      </linearGradient>
    </defs>
    <path d="M0 268 Q160 345 335 300" fill="none" stroke="#1fb2a3" stroke-width="4"/>
    <rect x="0" y="0" width="369" height="330" fill="url(#coverPhoto)" clip-path="url(#coverClip)" role="img" aria-label="Photo of cupped hands holding soil with a young seedling"/>
    <path d="M417 -6 A256 256 0 0 1 126 313" fill="none" stroke="#6e3d2c" stroke-width="8"/>
  </svg>
  <div class="brand cover-brand"><span class="dot"></span>Rootwise</div>
  <h1 class="cover-title">A STEERING<br>MANUAL</h1>
  <div class="cover-sub">LEADING EMPLOYEES WITH ADHD</div>
  <div class="author">
    <div class="name">Maren Holloway,</div>
    <div class="role">ADHD Coach</div>
    <div><b>Call:</b> 0100 200 300</div>
    <div><b>Email:</b> maren.holloway@example.com</div>
  </div>
</section>

<!-- Contents -->
<section class="page c2 r1">
  <header class="head"><span class="tag">A Steering Manual for the employee of staff with ADHD</span><span class="brand"><span class="dot"></span>Rootwise</span></header>
  <div class="body" style="top:60px">
    <h2 class="sec" style="margin-bottom:16px">TABLE <span>OF CONTENT</span></h2>
    <ul class="toc">
      <li class="main"><span class="t">Executive Summary</span><span class="fill"></span>1</li>
      <li class="main"><span class="t">1. Introduction to ADHD in the Workplace</span><span class="fill"></span>2</li>
      <li class="main"><span class="t">2. Legal Framework and Compliance</span><span class="fill"></span>2</li>
      <li class="lv2"><span class="t">2.1 The Equality Act</span><span class="fill"></span>2</li>
      <li class="lv2"><span class="t">2.2 European Convention on Human Rights (ECHR)</span><span class="fill"></span>2</li>
      <li class="lv2"><span class="t">2.3 Bullying and Harassment: Risks and Prevention</span><span class="fill"></span>3</li>
      <li class="lv2"><span class="t">2.4 Importance of Training for Awareness and a Non-Hostile Environment</span><span class="fill"></span>4</li>
      <li class="lv2"><span class="t">2.5 Proactive Measures: Occupational Health and Reasonable Adjustments</span><span class="fill"></span>4</li>
      <li class="main"><span class="t">3. Benefits and Challenges for ADHD Employees</span><span class="fill"></span>5</li>
      <li class="lv2"><span class="t">3.1 Benefits of Employing Individuals with ADHD</span><span class="fill"></span>5</li>
      <li class="lv2"><span class="t">3.2 Challenges Associated with ADHD in the Workplace</span><span class="fill"></span>5</li>
      <li class="main"><span class="t">4. Reasonable Adjustments and Support</span><span class="fill"></span>6</li>
      <li class="lv2"><span class="t">4.1 Flexible Working Arrangements</span><span class="fill"></span>6</li>
      <li class="lv2"><span class="t">4.2 Structuring the Work Environment</span><span class="fill"></span>6</li>
      <li class="lv2"><span class="t">4.3 Access to External and Professional Support</span><span class="fill"></span>6</li>
      <li class="main"><span class="t">5. Managing and Reporting to Employees with ADHD</span><span class="fill"></span>7</li>
      <li class="lv2"><span class="t">5.1 Advice for Managers</span><span class="fill"></span>7</li>
      <li class="lv2"><span class="t">5.2 Managing Performance Reviews and Feedback</span><span class="fill"></span>7</li>
      <li class="main"><span class="t">6. Advice for Working with ADHD Employees</span><span class="fill"></span>7</li>
      <li class="lv2"><span class="t">6.1 Cultivate a Culture of Understanding and Inclusion</span><span class="fill"></span>7</li>
      <li class="lv2"><span class="t">6.2 Respect Diverse Communication Styles</span><span class="fill"></span>8</li>
      <li class="lv2"><span class="t">6.3 Supportive Collaboration</span><span class="fill"></span>8</li>
      <li class="lv2"><span class="t">6.4 Give Space for Creative Thinking</span><span class="fill"></span>8</li>
      <li class="main"><span class="t">7. Performance Evaluation and Development for ADHD Employees</span><span class="fill"></span>8</li>
      <li class="lv2"><span class="t">7.1 Objective and Fair Evaluation Criteria</span><span class="fill"></span>8</li>
      <li class="lv2"><span class="t">7.2 Development Plans and Career Progression</span><span class="fill"></span>8</li>
      <li class="main"><span class="t">8. Monitoring and Reporting Discrimination</span><span class="fill"></span>8</li>
      <li class="lv2"><span class="t">8.1 Reporting Mechanisms</span><span class="fill"></span>8</li>
      <li class="lv2"><span class="t">8.2 Addressing Discrimination Complaints</span><span class="fill"></span>8</li>
      <li class="lv2"><span class="t">8.3 Zero Tolerance for Discrimination</span><span class="fill"></span>8</li>
      <li class="main"><span class="t">9. ADHD Disclosure and Confidentiality</span><span class="fill"></span>9</li>
      <li class="main"><span class="t">10. Additional Resources and Support</span><span class="fill"></span>9</li>
      <li class="lv2"><span class="t">10.1 Neurodiversity Awareness and Training Programs</span><span class="fill"></span>9</li>
      <li class="lv2"><span class="t">10.2 External Resources for ADHD Support</span><span class="fill"></span>9</li>
    </ul>
  </div>
</section>

<!-- Page 1 -->
<section class="page c3 r1">
  <header class="head"><span class="tag">A Steering Manual for the employee of staff with ADHD</span><span class="brand"><span class="dot"></span>Rootwise</span></header>
  <div class="body" style="top:44px">
    <p class="sub" style="font-size:5.4px">ABSTRACT</p>
    <p>Employees with ADHD bring valuable strengths such as creativity, energy, adaptability, and big-picture thinking. They may also face challenges with focus, time management, impulsivity, and sensitivity to criticism. This guide equips people leaders with practical strategies and supportive structures to help employees with ADHD thrive and drive team success.</p>
    <h2 class="sec" style="margin-top:28px">EXECUTIVE <span>SUMMARY</span></h2>
    <p>Employees with ADHD bring significant strengths to the workplace, including creativity, innovation, hyperfocus, high energy, adaptability, big-picture thinking, risk-taking, and strong empathy. These qualities make them valuable contributors in roles requiring problem-solving, vision, and momentum.</p>
    <p>At the same time, ADHD can present challenges such as inconsistent attention (driven by interest rather than importance), emotional hyperarousal, rejection sensitivity, impulsivity, distractibility, and time-blindness. These can impact task completion, focus, and response to feedback if not well-supported.</p>
    <p style="margin-bottom:1px"><b>KEY MANAGER STRATEGIES:</b></p>
    <ul class="keys">
      <li><b>Motivation &amp; Engagement:</b> Ensure work has purpose, novelty, challenge, or urgency to sustain focus and productivity. It helps if tasks are broken down into manageable chunks and timelines are short and urgent.</li>
      <li><b>Feedback &amp; Encouragement:</b> Provide frequent, authentic praise and constructive, forward-looking feedback. Emphasize strengths and effort to build confidence and psychological safety.</li>
      <li><b>Support &amp; Structure:</b> Offer coaching or organizational tools, encourage writing tasks down, and create systems that reduce overwhelm.</li>
    </ul>
    <p>By leveraging strengths and providing tailored support, managers can enable employees with ADHD to thrive, enhancing both individual performance and team success.</p>
  </div>
  <svg class="foot" style="height:110px"><use href="#wave"/></svg>
  <div class="foot-text"><span>Call: 0100 200 300 &nbsp;&nbsp;|&nbsp;&nbsp; maren.holloway@example.com</span><span>Pag 1 of 9</span></div>
</section>

<!-- Page 2 -->
<section class="page c1 r2">
  <header class="head"><span class="tag">A Steering Manual for the employee of staff with ADHD</span><span class="brand"><span class="dot"></span>Rootwise</span></header>
  <div class="body">
    <h2 class="sec">1. Introduction to ADHD <span>in the Workplace</span></h2>
    <p>ADHD is a lifelong difference in how attention, energy and emotion are regulated. Many adults reach senior roles before they are ever assessed, and most have built their own quiet strategies for coping. Leaders who understand this can turn daily friction into trust, and help talented people do their best work without masking or burning out along the way.</p>
    <p>This guide offers a practical starting point for managers who want to lead with care and clarity.</p>
    <h2 class="sec" style="margin-top:14px">2. Legal Framework <span>and Compliance</span></h2>
    <p class="sub">2.1 The Equality Act</p>
    <p>Under the Equality Act, ADHD can meet the definition of a disability where it has a substantial and long-term effect on daily activity. Employers have a duty to avoid discrimination and to make reasonable adjustments, whether or not a formal diagnosis has been shared, once they know or could reasonably be expected to know.</p>
    <p><b>Definition of Disability:</b> A condition counts when it has a substantial, long-term effect on the ability to carry out normal day-to-day activities. Most people with ADHD will meet this test, even when the effects are managed well with support, routine or medication at work.</p>
    <p class="sub">2.2 European Convention on Human Rights (ECHR)</p>
    <p>The Convention protects private life, dignity and freedom from unfair treatment. For employees with ADHD this means health details stay private, decisions are made fairly, and no one is treated less well because of how their mind works. Managers should keep this in view when handling records and conversations.<br>
    <span class="tick"></span><b>Equal Treatment and Dignity:</b> Every employee deserves respect and the same access to training, promotion and reward, with support shaped around their needs.<br>
    <span class="tick"></span><b>Fair Opportunity and Inclusion:</b> Remove barriers in hiring, review and progression so that ability, not style of working, decides outcomes.</p>
  </div>
  <svg class="foot"><use href="#wave"/></svg>
  <div class="foot-text"><span>Call: 0100 200 300 &nbsp;&nbsp;|&nbsp;&nbsp; maren.holloway@example.com</span><span>Pag 2 of 9</span></div>
</section>

<!-- Page 3 -->
<section class="page c2 r2">
  <header class="head"><span class="tag">A Steering Manual for the employee of staff with ADHD</span><span class="brand"><span class="dot"></span>Rootwise</span></header>
  <div class="body" style="top:54px">
    <p class="sub" style="margin-top:0">2.3 Bullying and Harassment: Risks and Prevention</p>
    <p>People with ADHD are more likely to face teasing, exclusion or unfair criticism at work. Much of it is subtle and goes unreported, so leaders need to watch closely, act early and make it safe to speak up.</p>
    <p><b>Overt Harassment Examples:</b> Mocking lateness or forgetfulness, public blame, name-calling, or jokes about attention and energy in front of colleagues.</p>
    <p><b>Subtle Harassment Examples:</b> Quiet patterns that wear people down over time and are easy to miss.</p>
    <p style="margin-top:8px"><span class="tick"></span><b>Being Ignored or Excluded:</b> Leaving someone out of meetings, chats or social events, or passing over their ideas without a fair hearing, so they slowly lose their voice within the team.</p>
    <p style="margin-top:8px"><span class="tick"></span><b>Microaggressions:</b> Small remarks such as “everyone gets distracted” or “just try harder” that dismiss a real condition and leave the person feeling unseen or doubted.</p>
    <p style="margin-top:8px"><span class="tick"></span><b>Withholding Support:</b> Delaying agreed adjustments, refusing tools that cost little, or treating requests for help as a sign of weakness rather than good sense.</p>
    <p style="margin-top:8px"><span class="tick"></span><b>Undermining Authority, Professional Abilities, and Experience:</b> Questioning competence in front of others, taking work away without reason, or giving credit for their ideas to someone else.</p>
    <p style="margin-top:8px"><span class="tick"></span><b>Giving Unsolicited Advice on ADHD:</b> Offering tips on diet, focus or medication without being asked, which can feel intrusive, however kindly it was meant.</p>
    <p style="margin-top:8px">Prevention starts with clear policy, visible leadership and prompt follow-up. Make it plain that these behaviours are not acceptable, and check in often with those most at risk.</p>
  </div>
  <svg class="foot"><use href="#wave"/></svg>
  <div class="foot-text"><span>Call: 0100 200 300 &nbsp;&nbsp;|&nbsp;&nbsp; maren.holloway@example.com</span><span>Pag 3 of 9</span></div>
</section>

<!-- Page 4 -->
<section class="page c3 r2">
  <header class="head"><span class="tag">A Steering Manual for the employee of staff with ADHD</span><span class="brand"><span class="dot"></span>Rootwise</span></header>
  <div class="body" style="top:54px">
    <p class="sub" style="margin-top:0">2.4 Importance of Training for Awareness and a Non-Hostile Environment</p>
    <p>Training helps teams understand ADHD as a difference rather than a flaw. When people know what to expect, they respond with patience, and small frictions stop growing into conflict. Regular sessions keep the message fresh and show that leaders take inclusion seriously across the whole business.</p>
    <p><b>Training Goals:</b> Build shared language, correct common myths, and give managers simple tools for everyday conversations, planning and feedback with neurodivergent staff.</p>
    <p><b>Awareness of Microaggressions and Subtle Discrimination:</b> Help teams notice the small comments and habits that exclude others, and practise better ways to respond in the moment.</p>
    <p><b>ECHR Compliance:</b> Make sure privacy, dignity and fair treatment are part of every process, from recruitment to review, and that records of health details are kept secure. Managers should know where to turn for advice when a situation is unclear, and should keep notes of decisions made.</p>
    <p class="sub">2.5 Proactive Measures: Occupational Health and Reasonable Adjustments</p>
    <p>Acting early saves time, stress and cost. Involve occupational health as soon as an employee asks for support, agree adjustments together, and review them at regular intervals so they keep working as roles and teams change over time.</p>
    <p><b>1. Involving Occupational Health Early:</b> A referral gives clear, expert advice on what will help and protects both the employee and the business.</p>
    <p><b>2. Assessing and Implementing Reasonable Adjustments:</b> Agree changes in writing, set a date to review them, and check in to see what is working well.</p>
  </div>
  <svg class="foot"><use href="#wave"/></svg>
  <div class="foot-text"><span>Call: 0100 200 300 &nbsp;&nbsp;|&nbsp;&nbsp; maren.holloway@example.com</span><span>Pag 4 of 9</span></div>
</section>

<!-- Page 5 -->
<section class="page c1 r3">
  <header class="head"><span class="tag">A Steering Manual for the employee of staff with ADHD</span><span class="brand"><span class="dot"></span>Rootwise</span></header>
  <div class="body">
    <h2 class="sec">3. Benefits and Challenges <span>for ADHD Employees</span></h2>
    <p class="sub">3.1 Benefits of Employing Individuals with ADHD</p>
    <p><b>1. Creative Thinking and Innovation:</b> Fresh ideas, new connections and a readiness to question how things have always been done.</p>
    <p><b>2. Adaptability and Resilience:</b> Comfortable with change and quick to recover, often at their best when plans shift.</p>
    <p><b>3. Hyperfocus:</b> Deep, sustained attention on work that matters to them, producing high-quality results fast.</p>
    <p><b>4. High Energy and Enthusiasm:</b> Bring drive and warmth that lift a team and keep projects moving forward.</p>
    <p><b>5. Risk-Taking and Problem Solving:</b> Willing to try bold solutions and think calmly in a crisis.</p>
    <p class="sub">3.2 Challenges Associated with ADHD in the Workplace</p>
    <p>The same brain that drives creativity can find routine tasks, long meetings and open-ended deadlines hard. These challenges are real but manageable, and most respond well to structure, clear goals and a supportive manager who asks rather than assumes.</p>
    <p><b>1. Attention Regulation:</b> Focus follows interest, so dull tasks may drift while exciting ones absorb hours.</p>
    <p><b>2. Time Management:</b> Estimating time and switching between tasks can be difficult without visible cues.</p>
    <p><b>3. Impulsivity:</b> Quick reactions in speech or decisions, which can be eased by pausing points.</p>
    <p><b>4. Memory and Organisational Difficulties:</b> Details may slip, so written notes and shared tools help greatly.</p>
  </div>
  <svg class="foot"><use href="#wave"/></svg>
  <div class="foot-text"><span>Call: 0100 200 300 &nbsp;&nbsp;|&nbsp;&nbsp; maren.holloway@example.com</span><span>Pag 5 of 9</span></div>
</section>

<!-- Page 6 -->
<section class="page c2 r3">
  <header class="head"><span class="tag">A Steering Manual for the employee of staff with ADHD</span><span class="brand"><span class="dot"></span>Rootwise</span></header>
  <div class="body">
    <h2 class="sec">4. Reasonable Adjustments <span>and Support</span></h2>
    <p class="sub">4.1 Flexible Working Arrangements</p>
    <p><span class="tick"></span><b>Flexible Hours:</b> Let people work when their focus is strongest, with core hours for shared team time and meetings.</p>
    <p><span class="tick"></span><b>Remote Working Options:</b> Quiet home days can reduce noise and interruption and make deep work far easier to achieve.</p>
    <p><span class="tick"></span><b>Compressed or Part-Time Schedules:</b> Fewer, fuller days can suit energy patterns and reduce fatigue over a busy week.</p>
    <p class="sub">4.2 Structuring the Work Environment</p>
    <p><span class="tick"></span><b>Quiet Workspaces:</b> Offer calm rooms, headphones or desks away from busy walkways to protect focus.</p>
    <p><span class="tick"></span><b>Visual and Task Management Tools:</b> Shared boards, checklists and reminders make priorities and deadlines easy to see.</p>
    <p><span class="tick"></span><b>Written Direction:</b> Follow spoken briefings with short written notes that confirm goals, owners and dates.</p>
    <p class="sub">4.3 Access to External and Professional Support</p>
    <p><span class="tick"></span>Coaching from a specialist helps employees build routines and strategies that fit their role and way of thinking.</p>
    <p><span class="tick"></span>Employee assistance services and occupational health can offer advice, counselling and practical guidance.</p>
    <p><span class="tick"></span>Government schemes may fund equipment, software or coaching, so check what support is available locally.</p>
  </div>
  <svg class="foot"><use href="#wave"/></svg>
  <div class="foot-text"><span>Call: 0100 200 300 &nbsp;&nbsp;|&nbsp;&nbsp; maren.holloway@example.com</span><span>Pag 6 of 9</span></div>
</section>

<!-- Page 7 -->
<section class="page c3 r3">
  <header class="head"><span class="tag">A Steering Manual for the employee of staff with ADHD</span><span class="brand"><span class="dot"></span>Rootwise</span></header>
  <div class="body">
    <h2 class="sec">5. Managing and Reporting to <span>Employees with ADHD</span></h2>
    <p class="sub">5.1 Advice for Managers</p>
    <p><span class="tick"></span><b>Set Clear, Measurable Objectives:</b> Short goals with visible milestones keep momentum and make progress easy to celebrate together.</p>
    <p><span class="tick"></span><b>Adapt Communication Style:</b> Ask how each person prefers to receive updates, and mix spoken, written and visual formats.</p>
    <p><span class="tick"></span><b>Leverage Their Strengths:</b> Match tasks to interests and talents wherever possible to unlock energy and focus.</p>
    <p><span class="tick"></span><b>Avoid Rigidity in Methods:</b> Judge the result, not the route, and allow people to work in the way that suits them.</p>
    <p><span class="tick"></span><b>Encourage Autonomy with Boundaries:</b> Give freedom to plan the work, with agreed check-ins and clear deadlines that keep everyone aligned.</p>
    <p class="sub">5.2 Managing Performance Reviews and Feedback</p>
    <p><span class="tick"></span><b>Focus on Outcomes and Effort:</b> Recognise what was achieved and the effort behind it, not only what was missed.</p>
    <p><span class="tick"></span><b>Offer Constructive, Specific Feedback:</b> Give clear examples and one or two next steps, and share feedback little and often.</p>
    <p><span class="tick"></span><b>Individual Development Plans:</b> Build plans around strengths and goals, reviewed together each quarter.</p>
    <h2 class="sec">6. Advice for Working <span>with ADHD Employees</span></h2>
    <p class="sub">6.1 Cultivate a Culture of Understanding and Inclusion</p>
    <p><span class="tick"></span>Talk openly about neurodiversity, model curiosity over judgement, and celebrate different ways of thinking across the team.</p>
  </div>
  <svg class="foot"><use href="#wave"/></svg>
  <div class="foot-text"><span>Call: 0100 200 300 &nbsp;&nbsp;|&nbsp;&nbsp; maren.holloway@example.com</span><span>Pag 7 of 9</span></div>
</section>

<!-- Page 8 -->
<section class="page c1 r4">
  <header class="head"><span class="tag">A Steering Manual for the employee of staff with ADHD</span><span class="brand"><span class="dot"></span>Rootwise</span></header>
  <div class="body">
    <p class="sub" style="margin-top:0">6.2 Respect Diverse Communication Styles</p>
    <p><span class="tick"></span>Allow time to process, accept written replies, and avoid reading fidgeting or interruptions as rudeness.</p>
    <p class="sub">6.3 Supportive Collaboration</p>
    <p><span class="tick"></span>Pair people whose strengths complement each other, share notes after meetings, and agree clear roles so that nothing important slips through the gaps.</p>
    <p class="sub">6.4 Give Space for Creative Thinking</p>
    <p><span class="tick"></span>Make room for brainstorming and new ideas, and give credit when those ideas shape the direction of the work.</p>
    <h2 class="sec">7. &nbsp;&nbsp;Performance Evaluation and Development <span>for ADHD<br>&nbsp;&nbsp;&nbsp;&nbsp;&nbsp;Employees</span></h2>
    <p class="sub">7.1 Objective and Fair Evaluation Criteria</p>
    <p><span class="tick"></span>Use clear, written criteria that focus on results, applied the same way to every person in the team.</p>
    <p class="sub">7.2 Development Plans and Career Progression</p>
    <p><span class="tick"></span>Offer stretch projects, mentoring and training so that people with ADHD can grow and progress into senior roles.</p>
    <h2 class="sec">8. Monitoring and Reporting <span>Discrimination</span></h2>
    <p class="sub">8.1 Reporting Mechanisms</p>
    <p><span class="tick"></span>Provide safe, simple and confidential ways to raise concerns, including an anonymous route.</p>
    <p class="sub">8.2 Addressing Discrimination Complaints</p>
    <p><span class="tick"></span>Investigate promptly and fairly, keep the person informed, and act on what is found without delay.</p>
    <p class="sub">8.3 Zero Tolerance for Discrimination</p>
    <p><span class="tick"></span>Make it clear that discrimination of any kind will never be accepted.</p>
  </div>
  <svg class="foot"><use href="#wave"/></svg>
  <div class="foot-text"><span>Call: 0100 200 300 &nbsp;&nbsp;|&nbsp;&nbsp; maren.holloway@example.com</span><span>Pag 8 of 9</span></div>
</section>

<!-- Page 9 -->
<section class="page c2 r4">
  <header class="head"><span class="tag">A Steering Manual for the employee of staff with ADHD</span><span class="brand"><span class="dot"></span>Rootwise</span></header>
  <div class="body">
    <h2 class="sec" style="margin-top:0">9. ADHD <span>Disclosure and Confidentiality</span></h2>
    <p>Sharing a diagnosis is a personal choice. Some employees tell their manager at once, others wait until trust is built, and some never disclose at all. Leaders can make disclosure feel safe by responding calmly, keeping details private and focusing on support.</p>
    <p><span class="tick"></span><b>Creating a Safe Environment</b><br>Show through words and actions that it is safe to ask.</p>
    <p><span class="tick"></span><b>Who to Disclose To</b><br>The employee decides who is told, whether a manager, HR or occupational health, and how much they share.</p>
    <p><span class="tick"></span><b>What to Disclose</b><br>Focus on what helps at work rather than medical detail, so the conversation stays practical, respectful and centred on support.</p>
    <p><span class="tick"></span><b>Confidentiality</b><br>Share information only with consent and only where it is needed.</p>
    <p><span class="tick"></span><b>Encouraging Voluntary Disclosure</b><br>Mention support options in onboarding and reviews, so employees know help is there whenever they choose to ask for it.</p>
    <p><span class="tick"></span><b>Supporting Disclosure Conversations</b><br>Listen, thank them for sharing, and agree next steps together with a date to follow up.</p>
    <h2 class="sec">10. Additional <span>Resources and Support</span></h2>
    <p class="sub">10.1 Neurodiversity Awareness and Training Programs</p>
    <p><span class="tick"></span>Run regular workshops for leaders and teams to build awareness and skills.</p>
    <p class="sub">10.2 External Resources for ADHD Support</p>
    <p><span class="tick"></span>National charities offer guides, helplines and peer groups for adults with ADHD.</p>
    <p><span class="tick"></span><b>Focus Forward Network:</b> A community hub with practical tips for neurodivergent professionals.</p>
    <p><span class="tick"></span><b>Clearpath Works:</b> Advice and resources for employers and employees.</p>
  </div>
  <svg class="foot"><use href="#wave"/></svg>
  <div class="foot-text"><span>Call: 0100 200 300 &nbsp;&nbsp;|&nbsp;&nbsp; maren.holloway@example.com</span><span>Pag 9 of 9</span></div>
</section>

<!-- Back cover -->
<section class="page c3 r4">
  <div class="back-ring"></div>
  <div class="back-photo" role="img" aria-label="Soft-focus photo of green foliage and sky"></div>
  <div class="brand back-brand"><span class="dot"></span>Rootwise</div>
  <div class="back-text">
    A STEERING MANUAL<br>LEADING EMPLOYEES WITH ADHD
    <div class="who">Maren Holloway, <span>ADHD Coach</span></div>
    <div class="contact"><b>Call:</b> 0100 200 300 &nbsp;|&nbsp; <b>Email:</b> maren.holloway@example.com</div>
  </div>
</section>
</body>
</html>
```